Amazing Sexy Elegant Eyecatching Wine Label

We need a label designed for our wine which is going to be produced very soon.

Needs to be on a grey scale, as colours increase the price per label dramatically.

Needs to have the "Crown" logo (file attached) included on the front and back label. Logo can be in black/white but can not be changed in any way, circle around the crown must stay there as well.

We are still unsure of whether to use "Harrowby Wine" or "Harrowby" as the brand for the label, if you could submit designs based around the two names we would appreciate that.

We will have 5 varieties, including; Sauvignon Blanc, Chardonnay, Pinot Gris, Riesling and Pinot Noir. So text needs to be easily changed.

We are after an image on the label which is modern and eye catching, even in a grey scale.

Please see other attached files for an idea we have done previously, we want something a bit more "designer" though. Some information on the label is a legal requirement and needs to be kept.

Target Market(s)

Wine Consumers

Requirements
Must have
• Crown Logo, Harrowby/Harrowby Wine brand, Grey Scale, Modern Design

```html
<!DOCTYPE html>
<html lang="en">
<head>
<meta charset="utf-8">
<title>Harrowby Wine – Sauvignon Blanc Label</title>
<link rel="stylesheet" href="https://fonts.googleapis.com/css2?family=Yellowtail&family=Oranienbaum&family=Montserrat:wght@700&display=swap">
<style>
  :root {
    --label-black: #0b0b0b;
    --frame-grey: #2a2a2a;
    --ink-white: #f2f2f2;
    --ink-soft: #a9a9a9;
    --ink-dim: #3a3a3a;
    --rule-grey: #8a8a8a;
  }
  html, body {
    margin: 0;
    padding: 0;
    width: 1200px;
    height: 2348px;
    overflow: hidden;
    background: var(--label-black);
  }
  .label {
    position: relative;
    width: 1200px;
    height: 2348px;
    background: var(--label-black);
    color: var(--ink-white);
    overflow: hidden;
  }
  .label-frame {
    position: absolute;
    inset: 0;
  }
  .brand-seal {
    position: absolute;
    left: 480px;
    top: 112px;
    width: 240px;
    height: 240px;
  }
  .brand-name {
    position: absolute;
    left: 0;
    width: 1200px;
    top: 440px;
    margin: 0;
    text-align: center;
    font-family: "Yellowtail", cursive;
    font-weight: 400;
    font-size: 156px;
    line-height: 1;
    color: var(--ink-white);
  }
  .brand-sub {
    position: absolute;
    left: 0;
    width: 1200px;
    top: 602px;
    text-align: center;
    font-family: "Oranienbaum", serif;
    font-size: 46px;
    line-height: 1;
    color: var(--ink-white);
  }
  .divider {
    position: absolute;
    left: 0;
    top: 680px;
    width: 1200px;
    height: 340px;
  }
  .variety {
    position: absolute;
    left: 0;
    width: 1200px;
    top: 1150px;
    margin: 0;
    text-align: center;
    font-family: "Oranienbaum", serif;
    font-weight: 400;
    font-size: 86px;
    line-height: 1;
    color: var(--ink-white);
  }
  .tasting-note {
    position: absolute;
    left: 0;
    width: 1200px;
    top: 1270px;
    text-align: center;
    font-family: "Oranienbaum", serif;
    font-size: 38px;
    line-height: 1;
    color: var(--ink-soft);
  }
  .signature-lockup {
    position: absolute;
    left: 0;
    width: 1200px;
    top: 1380px;
    display: flex;
    justify-content: center;
    align-items: center;
    gap: 28px;
    font-family: "Oranienbaum", serif;
    font-size: 36px;
    line-height: 1;
    color: var(--ink-white);
  }
  .signature-mark {
    width: 96px;
    height: 96px;
  }
  .abv {
    position: absolute;
    left: 96px;
    top: 2150px;
    font-family: "Montserrat", sans-serif;
    font-weight: 700;
    font-size: 92px;
    line-height: 1;
    color: var(--ink-white);
  }
  .abv-unit {
    font-size: 34px;
    letter-spacing: 1px;
  }
  .volume {
    position: absolute;
    right: 96px;
    top: 2150px;
    font-family: "Montserrat", sans-serif;
    font-weight: 700;
    font-size: 92px;
    line-height: 1;
    color: var(--ink-dim);
  }
  .volume-unit {
    font-size: 30px;
  }
</style>
</head>
<body>
<main class="label">
  <svg class="label-frame" width="1200" height="2348" viewBox="0 0 1200 2348" aria-hidden="true">
    <rect x="10" y="10" width="1180" height="2328" fill="none" stroke="var(--frame-grey)" stroke-width="20"/>
    <rect x="28" y="28" width="1144" height="2292" fill="none" stroke="var(--frame-grey)" stroke-width="3"/>
  </svg>

  <svg class="brand-seal" viewBox="0 0 240 240" aria-hidden="true">
    <circle cx="120" cy="120" r="114" fill="none" stroke="var(--ink-soft)" stroke-width="5"/>
  </svg>

  <h1 class="brand-name">Harrowby</h1>
  <div class="brand-sub">Wine</div>

  <svg class="divider" viewBox="0 0 1200 340" role="img" aria-label="Symmetrical ornamental flourish between two rows of dashed rules and diamonds">
    <defs>
      <radialGradient id="flourishTone" cx="50%" cy="50%" r="50%">
        <stop offset="0%" stop-color="#5a5a5a"/>
        <stop offset="100%" stop-color="#0b0b0b"/>
      </radialGradient>
    </defs>
    <line x1="280" y1="40" x2="560" y2="40" stroke="var(--rule-grey)" stroke-width="3" stroke-dasharray="8 6"/>
    <line x1="640" y1="40" x2="920" y2="40" stroke="var(--rule-grey)" stroke-width="3" stroke-dasharray="8 6"/>
    <path d="M600 22 L614 40 L600 58 L586 40 Z" fill="var(--ink-white)"/>
    <rect x="340" y="70" width="520" height="220" fill="url(#flourishTone)"/>
    <line x1="110" y1="160" x2="1090" y2="160" stroke="var(--ink-white)" stroke-width="3"/>
    <line x1="280" y1="280" x2="560" y2="280" stroke="var(--rule-grey)" stroke-width="3" stroke-dasharray="8 6"/>
    <line x1="640" y1="280" x2="920" y2="280" stroke="var(--rule-grey)" stroke-width="3" stroke-dasharray="8 6"/>
    <path d="M600 282 L614 300 L600 318 L586 300 Z" fill="var(--ink-white)"/>
  </svg>

  <h2 class="variety">Sauvignon Blanc</h2>
  <div class="tasting-note">Delightfully refreshing</div>

  <div class="signature-lockup">
    <span class="signature-name">Harrowby</span>
    <svg class="signature-mark" viewBox="0 0 96 96" aria-hidden="true">
      <circle cx="48" cy="48" r="40" fill="none" stroke="var(--ink-white)" stroke-width="4"/>
    </svg>
    <span class="signature-kind">Wine</span>
  </div>

  <div class="abv">11%<span class="abv-unit">VOL.</span></div>
  <div class="volume">750<span class="volume-unit">ML</span></div>
</main>
</body>
</html>
```